We need a designer to help us represent our unique approach to creating lesson plans for digital learning. At the Autumn Workshop for Online Fluency, held in Providence RI this July 13 - 18, we'll use your design with 100 teachers and then put it online to reach hundreds of thousands more.

We have a draft visual of our model that we like - but it's not pretty (Since we are not designers, it looks a little clunky).

Please create a simple and attractive design in two versions: (1) one that we can use as a 1-page printed handout and (2) one that we can use where teachers can fill in sections and write ideas under each section of the graphic.

Why you should bid on this job? We're a leading provider of digital and media literacy curriculum resources with a huge international and national audience. Working with us will establish your expertise in the area of educational multimedia design.

Target Market(s)

Elementary and secondary teachers in public schools

Industry/Entity Type

Digital

Font styles to use
Sans Serif

Requirements
Must have
• TITLE : Digital Literacy Curriculum Framework

1 page version - suitable for use as a poster or 1-page flyer

Fillable form version - suitable for use as a handout with spaces for teachers to write

```html
<!DOCTYPE html>
<html lang="en">
<head>
<meta charset="utf-8">
<title>Digital Literacy Curriculum Framework</title>
<link rel="stylesheet" href="https://fonts.googleapis.com/css2?family=Comfortaa:wght@300;400&display=swap">
<style>
  :root {
    --teal: #45a5b0;
    --paper: #f4f3e6;
    --ring: #e0dfb2;
    --ink: #8a7358;
    --rule: #7a6a50;
    --title: #f3e7a6;
    --self: #fccb98;
    --learners: #f9a54a;
    --community: #a7bfb0;
    --context: #fdd660;
    --white: #ffffff;
  }
  html, body {
    margin: 0;
    padding: 0;
    overflow: hidden;
    background: var(--paper);
  }
  .framework-sheet {
    display: block;
    width: 848px;
    height: 1200px;
    font-family: "Comfortaa", sans-serif;
  }
  .sheet-background { fill: var(--paper); }
  .title-band { fill: var(--teal); }
  .sheet-title {
    fill: var(--title);
    font-size: 30px;
    font-weight: 300;
    letter-spacing: 1.5px;
  }
  .quadrant-rule { stroke: var(--ink); stroke-width: 1.5; }
  .quadrant-label {
    fill: var(--ink);
    font-size: 20px;
    font-weight: 300;
    letter-spacing: 0.5px;
  }
  .outer-ring { fill: var(--ring); stroke: var(--rule); stroke-width: 2; }
  .ring-divider { stroke: var(--white); stroke-width: 1.5; }
  .ring-label {
    fill: var(--ink);
    font-size: 20px;
    font-weight: 300;
    letter-spacing: 0.5px;
  }
  .segment-self { fill: var(--self); }
  .segment-learners { fill: var(--learners); }
  .segment-community { fill: var(--community); }
  .segment-context { fill: var(--context); }
  .segment-gap { stroke: var(--white); stroke-width: 2; }
  .inner-edge { fill: none; stroke: var(--white); stroke-width: 2; }
  .segment-label {
    fill: var(--white);
    font-size: 18px;
    font-weight: 300;
  }
  .subject-halo { fill: none; stroke: var(--white); stroke-width: 2; }
  .subject-core { fill: var(--teal); }
  .subject-label {
    fill: var(--white);
    font-size: 20px;
    font-weight: 300;
  }
</style>
</head>
<body>
<svg class="framework-sheet" viewBox="0 0 848 1200" xmlns="http://www.w3.org/2000/svg">
  <defs>
    <path id="outer-label-track" d="M 777.6 623 A 350 350 0 1 1 77.6 623 A 350 350 0 1 1 777.6 623"/>
    <path id="inner-label-track" d="M 607.6 623 A 180 180 0 1 1 247.6 623 A 180 180 0 1 1 607.6 623"/>
  </defs>

  <rect class="sheet-background" width="848" height="1200"/>

  <!-- Title band -->
  <rect class="title-band" width="848" height="108"/>
  <text class="sheet-title" x="64" y="66">DIGITAL LITERACY CURRICULUM FRAMEWORK</text>

  <!-- Quadrant rules and labels -->
  <line class="quadrant-rule" x1="427.6" y1="108" x2="427.6" y2="217"/>
  <line class="quadrant-rule" x1="427.6" y1="1029" x2="427.6" y2="1200"/>
  <line class="quadrant-rule" x1="0" y1="627" x2="22" y2="627"/>
  <line class="quadrant-rule" x1="833" y1="627" x2="848" y2="627"/>

  <text class="quadrant-label" x="88" y="150">PURPOSE</text>
  <text class="quadrant-label" x="812" y="156" text-anchor="end">ASSESMENT</text>
  <text class="quadrant-label" x="83" y="1148">CONTENT</text>
  <text class="quadrant-label" x="792" y="1153" text-anchor="end">PEDAGOGY</text>

  <!-- Outer ring -->
  <circle class="outer-ring" cx="427.6" cy="623" r="406"/>
  <line class="ring-divider" x1="297.7" y1="444.2" x2="188.9" y2="294.5"/>
  <line class="ring-divider" x1="554.4" y1="442.0" x2="660.6" y2="290.5"/>
  <line class="ring-divider" x1="642.9" y1="672.7" x2="823.1" y2="714.3"/>
  <line class="ring-divider" x1="427.6" y1="844" x2="427.6" y2="1029"/>
  <line class="ring-divider" x1="214.1" y1="680.2" x2="35.4" y2="728.2"/>

  <text class="ring-label" text-anchor="middle"><textPath href="#outer-label-track" startOffset="75%">STANDARDS</textPath></text>
  <text class="ring-label" text-anchor="middle"><textPath href="#outer-label-track" startOffset="94.4%">WORK PRODUCTS</textPath></text>
  <text class="ring-label" text-anchor="middle"><textPath href="#outer-label-track" startOffset="13.6%">INSTRUCTIONAL STRATEGIES</textPath></text>
  <text class="ring-label" text-anchor="middle"><textPath href="#outer-label-track" startOffset="35.6%">TOOLS</textPath></text>
  <text class="ring-label" text-anchor="middle"><textPath href="#outer-label-track" startOffset="54.2%">TEXT</textPath></text>

  <!-- Inner segments -->
  <path class="segment-self" d="M 427.6 623 L 206.6 623 A 221 221 0 0 1 427.6 402 Z"/>
  <path class="segment-learners" d="M 427.6 623 L 427.6 402 A 221 221 0 0 1 648.6 623 Z"/>
  <path class="segment-community" d="M 427.6 623 L 648.6 623 A 221 221 0 0 1 427.6 844 Z"/>
  <path class="segment-context" d="M 427.6 623 L 427.6 844 A 221 221 0 0 1 206.6 623 Z"/>
  <line class="segment-gap" x1="206.6" y1="623" x2="648.6" y2="623"/>
  <line class="segment-gap" x1="427.6" y1="402" x2="427.6" y2="844"/>
  <circle class="inner-edge" cx="427.6" cy="623" r="221"/>

  <text class="segment-label" text-anchor="middle"><textPath href="#inner-label-track" startOffset="62.8%">Self</textPath></text>
  <text class="segment-label" text-anchor="middle"><textPath href="#inner-label-track" startOffset="86.4%">Learners</textPath></text>
  <text class="segment-label" text-anchor="middle"><textPath href="#inner-label-track" startOffset="11.4%">Community</textPath></text>
  <text class="segment-label" text-anchor="middle"><textPath href="#inner-label-track" startOffset="38.6%">Context</textPath></text>

  <!-- Subject hub -->
  <circle class="subject-halo" cx="427.6" cy="623" r="88"/>
  <circle class="subject-core" cx="427.6" cy="623" r="78"/>
  <text class="subject-label" x="427.6" y="630" text-anchor="middle">SUBJECT</text>
</svg>
</body>
</html>
```